We need UI/UX design for a public, informational website for The Copper Lantern.
The pages, structure, and content scope are already defined. Designers are required to work only on the UI/UX layout of these existing pages, focusing on clarity, hierarchy, spacing, and usability. Do not add, remove, rename, or reinterpret pages or content.
The website is strictly informational only. It must not include accounts, onboarding, payments, custody, escrow administration, marketplaces, dashboards, or any transactional functionality.
Scope of work
Apply UI/UX design to the predefined website pages
Design layout for text, images, notices, and sections
Ensure consistent components and layout patterns across page types
Optimize layouts for long form, compliance focused content
Content writing, page creation, and branding changes are out of scope.
Structure reference
The complete page list, hierarchy, and content definitions are provided in the technical documentation and must be treated as the primary source of truth.
A Figma link is provided only as a light visual reference for page existence and structure:
https://maple-kettle-48203917.plansite.example/
Designers must rely on the documentation for in depth and authoritative reference.
Brand guidelines
The Copper Lantern has existing brand guidelines and official logos, including light and dark versions. These assets will be provided and must be followed exactly. Designers must not redesign, alter, or reinterpret the brand identity.
Look and feel direction
The desired visual direction is inspired by:
https://quorvanta.example/
This reference is provided only to indicate:
Institutional and enterprise tone
Clean, modern typography
Strong hierarchy and generous whitespace
Editorial, content first layouts
Do not copy branding, layouts, components, or assets from the reference site.
Hero section direction
The hero section should follow a similar structural approach to the hero used on https://quorvanta.example/
, meaning:
Strong editorial framing
Clear headline hierarchy
Calm, institutional first impression
However, the background video must be Abu Dhabi focused, not generic or global. The video should visually reflect:
Abu Dhabi skyline or architectural language
Institutional, sovereign, long term infrastructure tone
Clean, slow, cinematic motion
No promotional, marketing, or lifestyle visuals
The hero must remain informational, restrained, and credible. No hype. No calls to invest. No implied participation.
Constraints
One global primary CTA only: “Continue to Brightmoor” (external)
All other interactions must be informational
No visuals or language implying offers, investment, eligibility, or participation
Clear separation between informational content and any external operational platforms
Deliverables
High fidelity UI/UX designs created in Figma, covering:
Desktop layouts
Tablet layouts where relevant
Mobile layouts
Complete Figma file(s) including:
All designed pages defined in the technical documentation
A reusable component library (headers, footers, cards, notice panels, forms, CTAs, typography styles, spacing system)
Clearly defined layout grids, spacing rules, and text styles
Proper use of components and variants, not detached frames
Designs prepared for developer handoff, including:
Clear layer naming and structure
Auto layout where appropriate
Consistent use of styles and components
Responsive behavior demonstrated within Figma
Notes or annotations only where necessary for clarity
No prototypes, interactions, or motion design beyond basic layout states, unless explicitly requested. The focus is static UI/UX clarity, not animation.
A detailed technical specification document and official brand assets will be provided.
Any designs delivered outside Figma, that alter structure or content, or that ignore the defined constraints, boundaries, or tone will be rejected.

```html
<!DOCTYPE html>
<html lang="en">
<head>
<meta charset="utf-8">
<title>The Copper Lantern</title>
<link rel="stylesheet" href="https://fonts.googleapis.com/css2?family=Archivo+Black&family=Inter:wght@400;500;600;700&family=Montserrat:wght@300;400&display=swap">
<style>
:root{
  --ink:#111418;
  --body:#2a2f36;
  --white:#ffffff;
  --blue:#48a0f7;
  --blue-solid:#44a0f6;
  --violet:#7d6cf6;
  --accent:#8a63f0;
  --pale:#eaf4fd;
  --navy:#0b1320;
  --hero-top:#0d2a6e;
  --hero-bottom:#0a0f2a;
  --rule-light:rgba(255,255,255,.75);
}
*{margin:0;padding:0;box-sizing:border-box}
html,body{width:1200px;height:3863px;overflow:hidden}
body{font-family:"Inter",sans-serif;color:var(--body);background:var(--white);position:relative}
.heading{font-family:"Archivo Black",sans-serif;color:var(--ink);text-transform:uppercase;letter-spacing:.3px}
.abs{position:absolute}

/* header */
.site-header{position:absolute;left:0;top:0;width:1200px;height:99px;background:var(--white);border-bottom:2px solid #1d4fa3}
.brand-name{position:absolute;left:22px;top:38px;font-family:"Montserrat",sans-serif;font-weight:400;font-size:15px;color:var(--ink);letter-spacing:.4px;white-space:nowrap}
.nav-item{position:absolute;top:39px;display:inline-flex;align-items:center;gap:6px;font-size:11.5px;font-weight:500;color:var(--ink);white-space:nowrap}
.nav-item.active{color:var(--accent);font-weight:600}
.nav-item svg{width:9px;height:9px}
.cta-primary{position:absolute;left:951px;top:24px;width:229px;height:44px;background:linear-gradient(90deg,var(--blue),var(--violet));color:var(--white);font-size:12px;font-weight:700;display:flex;align-items:center;justify-content:center;gap:10px;letter-spacing:.3px;white-space:nowrap}

/* hero */
.hero{position:absolute;left:0;top:99px;width:1200px;height:576px;background:linear-gradient(180deg,var(--hero-top) 0%,#163b8f 45%,var(--hero-bottom) 100%)}
.hero-title{position:absolute;left:483px;top:110px;width:561px;border-top:1.5px solid var(--rule-light);border-bottom:1.5px solid var(--rule-light);padding:22px 0 18px;text-align:center;color:var(--white);font-size:42px;white-space:nowrap}

/* about */
.about-photo{left:150px;top:736px;width:429px;height:365px;background:linear-gradient(180deg,#8fb6df 0%,#d8e2ea 45%,#c9b7a8 75%,#9a7f86 100%)}
.section-title{font-size:28px;line-height:1.2}
.rule{width:54px;height:1.5px;background:var(--ink)}
.copy{font-size:12.8px;line-height:24px;text-align:justify;color:var(--body)}
.copy p+p{margin-top:20px}

/* bands */
.band-gradient{position:absolute;left:0;width:1200px;background:linear-gradient(90deg,var(--blue) 0%,#5d95f7 60%,var(--violet) 100%)}
.band-solid{position:absolute;left:0;width:1200px;background:var(--blue-solid)}
.center-title{position:absolute;left:0;width:1200px;text-align:center;color:var(--white);font-size:28px}
.center-rule{position:absolute;left:573px;width:54px;height:1.5px;background:var(--rule-light)}
.center-copy{position:absolute;left:190px;width:820px;text-align:center;color:var(--white);font-size:16.5px;line-height:25px}

/* layers */
.layer{position:absolute;top:2098px;width:300px;text-align:center;color:var(--white)}
.layer svg{width:66px;height:66px;display:block;margin:0 auto 42px}
.layer h3{font-family:"Inter",sans-serif;font-weight:700;font-size:16.5px;letter-spacing:.3px;margin-bottom:10px}
.layer p{font-size:13.5px;line-height:18px}
.layer-divider{position:absolute;top:2098px;width:1.5px;height:213px;background:var(--rule-light)}

.illustration{position:absolute}

/* footer */
.site-footer{position:absolute;left:0;top:3533px;width:1200px;height:330px;background:var(--navy);color:#c7d1de}
.footer-brand{position:absolute;left:152px;top:115px;font-family:"Montserrat",sans-serif;color:var(--white);font-size:24px;font-weight:300;letter-spacing:.4px;white-space:nowrap}
.footer-col{position:absolute;top:47px;font-size:12px;line-height:19.5px}
.footer-col h4{color:var(--blue);font-weight:700;font-size:13px;margin-bottom:6px;letter-spacing:.3px}
.social{display:flex;gap:6px;margin-top:6px}
.social span{width:33px;height:33px;border-radius:50%;background:var(--blue)}
.footer-rule{position:absolute;left:150px;top:244px;width:900px;height:1px;background:#1f2a3a}
.copyright{position:absolute;left:0;top:282px;width:1200px;text-align:center;font-size:12px;color:#c7d1de}
</style>
</head>
<body>

<header class="site-header">
  <span class="brand-name">THE COPPER LANTERN</span>
  <span class="nav-item active" style="left:241px">HOME</span>
  <span class="nav-item" style="left:311px">FRAMEWORK <svg viewBox="0 0 10 10"><path d="M1 3l4 4 4-4" fill="none" stroke="#111418" stroke-width="1.5"/></svg></span>
  <span class="nav-item" style="left:431px">PROJECTS <svg viewBox="0 0 10 10"><path d="M1 3l4 4 4-4" fill="none" stroke="#111418" stroke-width="1.5"/></svg></span>
  <span class="nav-item" style="left:534px">BRIGHTMOOR <svg viewBox="0 0 10 10"><path d="M1 3l4 4 4-4" fill="none" stroke="#111418" stroke-width="1.5"/></svg></span>
  <span class="nav-item" style="left:652px">INSIGHTS <svg viewBox="0 0 10 10"><path d="M1 3l4 4 4-4" fill="none" stroke="#111418" stroke-width="1.5"/></svg></span>
  <span class="nav-item" style="left:748px">COMPANY <svg viewBox="0 0 10 10"><path d="M1 3l4 4 4-4" fill="none" stroke="#111418" stroke-width="1.5"/></svg></span>
  <span class="nav-item" style="left:843px">CONTACT <svg viewBox="0 0 10 10"><path d="M1 3l4 4 4-4" fill="none" stroke="#111418" stroke-width="1.5"/></svg></span>
  <div class="cta-primary">CONTINUE TO BRIGHTMOOR <svg width="10" height="14" viewBox="0 0 10 14"><path d="M2 1l6 6-6 6" fill="none" stroke="#fff" stroke-width="2"/></svg></div>
</header>

<section class="hero" role="img" aria-label="Night skyline of towers and a lit palace under blue searchlights">
  <h1 class="hero-title heading">The Copper Lantern</h1>
</section>

<section class="about">
  <div class="abs about-photo" role="img" aria-label="Palace courtyard with white domed building under a cloudy sky"></div>
  <h2 class="abs heading section-title" style="left:621px;top:730px">The Copper Lantern</h2>
  <div class="abs rule" style="left:621px;top:783px"></div>
  <div class="abs copy" style="left:621px;top:817px;width:426px">
    <p>The Copper Lantern is a governance and project origination group. Its purpose is to define structural standards and oversight principles for complex initiatives that may involve multiple parties, staged execution, and long-term accountability. This website publishes those standards and explains how responsibilities are separated across governance, operations, and project-level execution.</p>
    <p>This site is informational. It does not provide onboarding, account access, eligibility checks, custody of funds, escrow administration, or transaction execution. Where operational workflows exist, they are provided through a separate operating platform under separate terms and policies.</p>
  </div>
</section>

<section class="band-gradient" style="top:1160px;height:318px">
  <h2 class="center-title heading" style="top:58px">Governance and Project Origination</h2>
  <div class="center-rule" style="top:124px"></div>
  <p class="center-copy" style="top:164px">Governance in this context refers to the standards that determine how projects are structured and how oversight is described. Origination refers to the initial design and definition of an initiative, including role separation, reporting expectations, and boundary setting before execution begins. The Copper Lantern focuses on these governance-level elements rather than on operating day-to-day workflows.</p>
</section>

<section class="roles">
  <h2 class="abs heading section-title" style="left:147px;top:1546px">Clear Role Separation</h2>
  <div class="abs rule" style="left:148px;top:1606px"></div>
  <p class="abs copy" style="left:148px;top:1645px;width:504px">The ecosystem is designed around clear separation of responsibilities. Governance activities belong at the framework layer. Operational workflows, where available, belong on a separate operating platform designed for process execution and recordkeeping. Assets and project execution, where applicable, belong at the project level through ring-fenced structures created for specific initiatives. This separation is intended to reduce ambiguity and help stakeholders understand who is responsible for what.</p>
  <div class="illustration" style="left:745px;top:1545px;width:281px;height:282px;border-radius:50%;background:linear-gradient(180deg,#dfeafe 0%,#6f9cf7 60%,#5a8bf6 100%)" role="img" aria-label="Blue illustration of a tree and mountains on a floating island"></div>
</section>

<section class="band-solid" style="top:1890px;height:578px">
  <h2 class="center-title heading" style="top:52px">How the Ecosystem Works</h2>
  <p class="abs" style="left:0;top:96px;width:1200px;text-align:center;color:#fff;font-size:16px">At a high level, the ecosystem can be understood as three layers:</p>
  <div class="center-rule" style="top:142px"></div>
</section>
<div class="layer" style="left:95px">
  <svg viewBox="0 0 66 66"><g fill="none" stroke="#fff" stroke-width="3"><path d="M8 22L33 8l25 14z"/><path d="M10 26h46M10 56h46M6 61h54"/><path d="M17 30v22M29 30v22M37 30v22M49 30v22"/></g></svg>
  <h3>GOVERNANCE</h3>
  <p>defines standards, explains<br>role boundaries, and publishes<br>framework information.</p>
</div>
<div class="layer-divider" style="left:404px"></div>
<div class="layer" style="left:450px">
  <svg viewBox="0 0 66 66"><g fill="none" stroke="#fff" stroke-width="3"><path d="M12 26a22 22 0 0 1 38-10M54 40a22 22 0 0 1-38 10"/><path d="M50 8v9h-9M16 58v-9h9"/><circle cx="33" cy="33" r="9"/><path d="M33 18v6M33 42v6M18 33h6M42 33h6M22 22l4 4M40 40l4 4M44 22l-4 4M26 40l-4 4"/></g></svg>
  <h3>OPERATIONS</h3>
  <p>manages workflow processes<br>such as documentation steps and<br>record-anchored audit events through<br>a separate platform.</p>
</div>
<div class="layer-divider" style="left:774px"></div>
<div class="layer" style="left:780px">
  <svg viewBox="0 0 66 66"><g fill="none" stroke="#fff" stroke-width="3"><path d="M14 6h26l10 10v20M14 6v52h22"/><path d="M20 20h18M20 28h22M20 36h14M20 44h10"/><circle cx="48" cy="50" r="11"/><path d="M43 50l4 4 7-7"/></g></svg>
  <h3>PROJECT EXECUTION</h3>
  <p>occurs at the project level through<br>dedicated structures that hold<br>responsibilities and assets where<br>applicable.</p>
</div>
<p class="center-copy" style="top:2365px;left:205px;width:790px;font-size:16.5px;line-height:26px">This website focuses on the governance layer and provides links to learn about structural concepts such as role separation, escrow and milestone framing, and recordkeeping terminology.</p>

<section class="escrow">
  <h2 class="abs heading section-title" style="left:168px;top:2526px;line-height:36px">Independent<br>Escrow and<br>Milestone<br>Oversight</h2>
  <div class="abs" style="left:449px;top:2530px;width:1.5px;height:136px;background:var(--ink)"></div>
  <p class="abs copy" style="left:510px;top:2533px;width:515px">Some initiatives use independent escrow arrangements to coordinate staged releases linked to milestone completion. Escrow can support execution discipline by requiring defined evidence before releases occur. Escrow does not guarantee outcomes, timelines, or success, and it is not administered by this website operator. This site describes the concept for clarity and transparency.</p>
</section>

<section class="workflows abs" style="left:0;top:2735px;width:1200px;height:400px;background:var(--pale)">
  <div class="illustration" style="left:160px;top:58px;width:293px;height:290px;border-radius:50%;background:radial-gradient(circle,#a7b7fa 0%,#6a93f6 70%)" role="img" aria-label="Four gears circling a document, joined by arrows"></div>
  <h2 class="abs heading section-title" style="left:520px;top:84px;line-height:42px">Where Operational<br>Workflows Happen</h2>
  <div class="abs rule" style="left:520px;top:187px"></div>
  <p class="abs copy" style="left:520px;top:220px;width:521px">Operational workflows, including any onboarding or workflow participation where permitted, occur on a separate operating platform under separate terms and policies. If you need operational access, use the Brightmoor page on this site to navigate externally. This website does not host those workflows.</p>
</section>

<section class="band-gradient" style="top:3135px;height:398px">
  <h2 class="center-title heading" style="top:62px">Contact and Inquiries</h2>
  <div class="center-rule" style="top:130px"></div>
  <p class="center-copy" style="top:167px;left:245px;width:710px">If you have questions about governance framework concepts, role boundaries, or information published on this website, you can contact the team using the Contact page. Do not submit sensitive personal data through public forms.</p>
  <div class="abs" style="left:486px;top:277px;width:228px;height:47px;background:#fff;color:var(--blue);font-weight:700;font-size:16px;display:flex;align-items:center;justify-content:center">CONTACT THE TEAM</div>
</section>

<footer class="site-footer">
  <span class="footer-brand">THE COPPER LANTERN</span>
  <div class="footer-col" style="left:500px">
    <h4>MENU</h4>
    Framework<br>Projects<br>Brightmoor<br>Insights<br>Company<br>Contact<br>Glossary
  </div>
  <div class="footer-col" style="left:660px">
    <h4>LINKS</h4>
    Legal (Index)<br>Terms of Use<br>Privacy Policy<br>Cookie Policy<br>Disclaimer &amp; Risk Notices<br>Acceptable Use Policy<br>Accessibility Statement
  </div>
  <div class="footer-col" style="left:852px">
    <h4>FOLLOW US</h4>
    <div class="social"><span></span><span></span><span></span><span></span><span></span></div>
  </div>
  <div class="footer-rule"></div>
  <p class="copyright">Copyright © 2026 All Rights Reserved</p>
</footer>

</body>
</html>
```